Varden Institute for Restorative Care

I need a full informational website for my medical practice. I would like to use my logo and also include a lot of emblems/pictures (also a picture of me in a white coat). The website should have a function for people to inquire and send me messages. I will be offering needle-less regenerative injection therapy, stem cell treatments, bioidentical hormone therapy, treatment for chronic illness, neurodegenerative diseases, skin rejuvenation, hair restoration, male enhancement, female enhancement, and anti-aging. The practice will not be accepting insurance and will be cash/credit card only.
A good example of written content and functionality is this website:
http://thebrvx.example/. However, I want different theme and tones.
Target Market(s)
High end clientele in Los Angeles, Southern California. Health minded people who are interested in living better and longer and can afford anti-aging treatments. Men and women who want to improve sexual health and wellbeing.
Requirements
Must have
- 1. I will need to be able to move the site to other servers (needed for site speed)
- 2. Site must be build on WordPress
- 3. Full admin credentials for domain, cpanel, wordpress, ftp.
- 4. No third party interaction on development and content deployment once the site is on different servers
- 5. I will need the ability to add content and links to the site
- 6. I will need the ability to optimize the site for speed
- 7. I will need to ability to modify URLs so they are more SEO friendly
Nice to have
- pictures of stem cells, health improvement and regeneration, beauty, youthful individuals, older healthy and happy individuals. Medical designs.
Should not have
- flowers, dna

```html
<!DOCTYPE html>
<html lang="en">
<head>
<meta charset="utf-8">
<title>Varden Institute for Restorative Care</title>
<link rel="stylesheet" href="https://fonts.googleapis.com/css2?family=Cinzel:wght@400;600;700&family=Open+Sans:wght@400;600&display=swap">
<style>
:root{
  --navy:#1c2d6b;
  --teal:#18a58a;
  --teal-dark:#12876f;
  --teal-text:#1e9c8a;
  --band-a:#8fd6cf;
  --band-b:#a9d6ec;
  --ink:#333a40;
  --muted:#6b7177;
  --line:#d6dadd;
  --paper:#ffffff;
  --soft:#f2f4f5;
  --photo-skin:#d9b9a4;
  --photo-grey:#b8bcc0;
}
*{box-sizing:border-box;margin:0;padding:0}
html,body{width:1200px;height:4337px;overflow:hidden;background:var(--paper)}
body{font-family:"Open Sans",Arial,sans-serif;color:var(--ink);position:relative}
section,header,footer{position:absolute;left:0;width:1200px}
.abs{position:absolute}
.serif{font-family:"Cinzel",Georgia,serif}
.brand{display:flex;align-items:center;gap:12px;font-family:"Cinzel",Georgia,serif;font-weight:700;color:var(--navy)}
.brand-dot{border-radius:50%;background:var(--teal)}
.photo{position:absolute}
.btn-wrap{position:absolute;display:flex;gap:10px}
.btn{background:var(--teal);color:#fff;font-size:15px;font-weight:600;display:flex;align-items:center;justify-content:center;border:2px solid #fff;height:40px}
.btn-arrow{width:30px;height:40px;background:var(--teal);border:2px solid #fff;display:flex;align-items:center;justify-content:center}
.heading{font-family:"Cinzel",Georgia,serif;color:var(--navy);font-weight:600;text-align:center;width:1200px;position:absolute;left:0}
.divider{position:absolute;display:flex;align-items:center;gap:8px}
.divider i{display:block;height:2px;background:var(--teal)}
.divider b{display:block;width:22px;height:22px;border-radius:50%;border:3px solid var(--teal)}

/* header */
.site-header{top:0;height:130px;background:#fff}
.site-header .brand{position:absolute;left:60px;top:22px;font-size:30px}
.phone{position:absolute;right:95px;top:16px;font-size:17px;color:var(--ink);display:flex;align-items:center;gap:8px}
.nav{position:absolute;right:70px;top:64px;display:flex;gap:32px;font-family:"Cinzel",Georgia,serif;font-size:17px;color:var(--navy);font-weight:600}
.nav .active{color:var(--teal);border-bottom:2px solid var(--teal);padding-bottom:4px}

/* hero */
.hero{top:130px;height:544px;background:linear-gradient(90deg,#eef0f1,#fafbfb 50%,#eef0f1)}
.hero-title{position:absolute;left:380px;width:440px;top:150px;text-align:center;font-family:"Cinzel",Georgia,serif;font-size:37px;line-height:55px;color:var(--teal-text);font-weight:600}

/* about */
.about{top:674px;height:535px;background:linear-gradient(100deg,var(--band-a),var(--band-b))}
.about p{position:absolute;left:150px;width:900px;text-align:center;color:#23313a}

/* services */
.services{top:1209px;height:1047px;background:#fff}
.tile{position:absolute;width:232px;height:232px;overflow:hidden}
.tile .cap{position:absolute;left:0;bottom:0;width:100%;height:50px;background:rgba(60,50,45,.72);color:#fff;font-size:14px;text-align:center;display:flex;align-items:center;justify-content:center;line-height:17px}

/* doctor */
.doctor{top:2256px;height:399px;background:linear-gradient(100deg,#7ed0c6,var(--band-b))}
.doctor h2{position:absolute;left:113px;top:70px;font-family:"Cinzel",Georgia,serif;font-size:31px;color:var(--navy);font-weight:600}
.doctor p{position:absolute;left:113px;top:156px;width:570px;font-size:14px;line-height:21px;color:#1e2a30}

/* testimonials */
.testimonials{top:2655px;height:497px;background:#fff}
.quote{position:absolute;left:375px;top:210px;width:640px;font-size:14px;line-height:22px;color:#444}
.dots{position:absolute;left:538px;top:402px;display:flex;gap:8px}
.dots span{width:8px;height:8px;border-radius:50%;background:#c8ccd0}
.dots span:first-child{background:var(--teal)}

/* cta */
.cta{top:3152px;height:284px;background:linear-gradient(100deg,#8dd6cd,#7fbfe0)}
.cta h3{position:absolute;left:100px;width:1000px;top:68px;text-align:center;font-family:"Cinzel",Georgia,serif;font-size:28px;line-height:44px;color:#fff;font-weight:600}

/* contact */
.contact{top:3436px;height:555px;background:#fff}
.field{position:absolute;height:40px;border:1px solid var(--line);font-size:11px;color:#8a8f94;padding:12px 14px;letter-spacing:.5px}
.submit{position:absolute;left:324px;top:425px;width:552px;height:44px;background:var(--teal);color:#fff;font-size:15px;display:flex;align-items:center;justify-content:center;letter-spacing:.5px}

/* footer */
.foot-nav{top:3991px;height:72px;background:var(--soft);border-top:1px solid #e4e6e8;border-bottom:1px solid #e4e6e8}
.foot-nav ul{list-style:none;display:flex;justify-content:center;gap:75px;padding-top:30px;font-size:12px;color:#333}
.site-footer{top:4063px;height:232px;background:#fff}
.site-footer h4{font-size:16px;font-weight:400;color:#333;position:absolute}
.contact-line{position:absolute;left:781px;display:flex;gap:10px;font-size:13px;color:#444;align-items:flex-start}
.social{position:absolute;left:515px;top:148px;display:flex;gap:8px}
.social span{width:24px;height:24px;border-radius:50%}
.copyright{top:4295px;height:42px;background:var(--soft);text-align:center;font-size:12px;color:#555;padding-top:14px}
</style>
</head>
<body>

<header class="site-header">
  <div class="brand"><span class="brand-dot" style="width:18px;height:18px"></span>VARDEN</div>
  <div class="phone">
    <svg width="16" height="16" viewBox="0 0 24 24"><path fill="#333a40" d="M6.6 10.8a15 15 0 0 0 6.6 6.6l2.2-2.2c.3-.3.7-.4 1-.2 1.1.4 2.3.6 3.6.6.6 0 1 .4 1 1V20c0 .6-.4 1-1 1A17 17 0 0 1 3 4c0-.6.4-1 1-1h3.5c.6 0 1 .4 1 1 0 1.3.2 2.5.6 3.6.1.3 0 .7-.2 1z"/></svg>
    123-456-7890
  </div>
  <nav class="nav">
    <span class="active">HOME</span><span>ABOUT US</span><span>SERVICES</span><span>SCIENCE</span><span>TESTIMONIALS</span><span>CONTACT US</span>
  </nav>
</header>

<section class="hero">
  <div class="photo" role="img" aria-label="Smiling young man, shoulders bare" style="left:0;top:0;width:405px;height:544px;background:linear-gradient(90deg,#e6e8ea,#cfa88f 55%,#e9ebec)"></div>
  <div class="photo" role="img" aria-label="Young woman with smooth skin and hair tied back" style="right:0;top:0;width:370px;height:544px;background:linear-gradient(270deg,#e4e6e8,#e2c2ae 55%,#eff1f2)"></div>
  <h1 class="hero-title">Varden Institute For Restorative Care, Focuses On Cutting Edge Cell Therapy</h1>
</section>

<section class="about">
  <div class="abs brand-dot" style="left:584px;top:88px;width:32px;height:32px"></div>
  <h2 class="heading" style="top:158px;font-size:32px">ABOUT VARDEN</h2>
  <div class="divider" style="left:485px;top:204px"><i style="width:230px;height:2px;background:var(--navy)"></i></div>
  <p style="top:238px;font-size:14px;line-height:22px">Lorem ipsum dolor sit amet, consectetur adipiscing elit, sed diam nonummy nibh euismod tincidunt ut laoreet dolore magna aliquam erat volutpat. Ut wisi enim ad minim veniam, quis nostrud exerci tation ullamcorper suscipit lobortis nisl ut aliquip</p>
  <p style="top:320px;font-size:12.5px;line-height:20px">quis nostrud exerci tation ullamcorper suscipit lobortis nisl ut aliquip ex ea commodo consequat. Duis autem vel eum iriure dolor in hendrerit in vulputate velit esse molestie consequat, vel illum dolore eu feugiat nulla facilisis at vero eros et accumsan et iusto odio dignissim qui blandit praesent luptatum zzril delenit augue duis dolore te feugait nulla facilisi. Lorem ipsum dolor sit amet, consectetuer adipiscing elit, sed diam nonummy nibh euismod tincidunt ut l</p>
  <div class="btn-wrap" style="left:523px;top:432px">
    <div class="btn" style="width:116px">Read More</div>
    <div class="btn-arrow"><svg width="12" height="12" viewBox="0 0 12 12"><path d="M2 4l4 4 4-4" stroke="#fff" stroke-width="2" fill="none"/></svg></div>
  </div>
</section>

<section class="services">
  <h2 class="heading" style="top:68px;font-size:34px">OUR SERVICES</h2>
  <div class="divider" style="left:488px;top:144px"><i style="width:95px"></i><b></b><i style="width:95px"></i></div>

  <div class="tile" style="left:113px;top:173px;background:linear-gradient(135deg,#7ecfd0,#9fc7e6)" role="img" aria-label="Stem cell treatments, cells under a microscope">
    <div class="abs" style="left:0;top:70px;width:100%;text-align:center;color:#fff;font-size:17px;line-height:24px">Stem Cell<br>Treatments</div>
    <svg class="abs" style="left:98px;top:130px" width="36" height="36" viewBox="0 0 24 24"><circle cx="10" cy="10" r="6" stroke="#2a5f86" stroke-width="2.5" fill="none"/><path d="M14.5 14.5L21 21" stroke="#2a5f86" stroke-width="3"/></svg>
  </div>
  <div class="tile" style="left:359px;top:173px;background:linear-gradient(160deg,#d9c0b0,#b09584)" role="img" aria-label="Woman receiving facial treatment"><div class="cap">Needle-less Regenerative<br>Injection Therapy</div></div>
  <div class="tile" style="left:604px;top:173px;background:linear-gradient(160deg,#c9967e,#9a6d5a)" role="img" aria-label="Mature woman with red hair smiling"><div class="cap">Bioidentical Hormone<br>Therapy</div></div>
  <div class="tile" style="left:853px;top:173px;background:linear-gradient(160deg,#cfc4bd,#8f8c90)" role="img" aria-label="Woman holding her head in discomfort"><div class="cap">Treatment For Chronic<br>Illness</div></div>

  <div class="tile" style="left:113px;top:454px;background:linear-gradient(160deg,#9d9a98,#6f6a66)" role="img" aria-label="Older man in thought"><div class="cap">Neurodegenerative<br>Diseases</div></div>
  <div class="tile" style="left:359px;top:454px;background:linear-gradient(160deg,#d8cfc9,#a89a92)" role="img" aria-label="Skin treatment device on a face"><div class="cap">Skin<br>Rejuvenation</div></div>
  <div class="tile" style="left:604px;top:454px;background:linear-gradient(160deg,#8c6e60,#6a87a8)" role="img" aria-label="Gloved hands examining hair"><div class="cap">Hair<br>Restoration</div></div>
  <div class="tile" style="left:853px;top:454px;background:linear-gradient(160deg,#d8b8a4,#a78470)" role="img" aria-label="Smiling couple"><div class="cap">Male<br>Enhancement</div></div>

  <div class="tile" style="left:113px;top:734px;background:linear-gradient(160deg,#b99784,#7d6154)" role="img" aria-label="Thoughtful woman"><div class="cap">Female Enhancement</div></div>
  <div class="tile" style="left:359px;top:734px;background:linear-gradient(160deg,#ccb4a4,#96786a)" role="img" aria-label="Woman receiving anti-aging treatment"><div class="cap">Anti - Aging</div></div>

  <div class="abs brand" style="left:706px;top:830px;font-size:50px;gap:16px"><span class="brand-dot" style="width:30px;height:30px"></span>VARDEN</div>
</section>

<section class="doctor">
  <div class="photo" role="img" aria-label="Doctor in a white coat, arms crossed" style="left:708px;top:48px;width:333px;height:351px;background:linear-gradient(180deg,#cfa98f 0%,#caa58d 35%,#f4f6f7 45%,#e8ecee 100%)"></div>
  <h2>ABOUT DR. LOREN IPSUM</h2>
  <div class="divider" style="left:113px;top:118px"><b></b><i style="width:120px"></i></div>
  <p>quis nostrud exerci tation ullamcorper suscipit lobortis nisl ut aliquip ex ea commodo consequat. Duis autem vel eum iriure dolor in hendrerit in vulputate velit esse molestie consequat, vel illum dolore eu feugiat nulla facilisis at vero eros et accumsan et iusto odio dignissim qui blandit praesent luptatum zzril delenit augue duis dolore te feugait nulla facilisi. Lorem ipsum dolor sit amet, consectetuer adipiscing</p>
  <div class="btn-wrap" style="left:113px;top:296px">
    <div class="btn" style="width:116px">Read More</div>
    <div class="btn-arrow"><svg width="12" height="12" viewBox="0 0 12 12"><path d="M2 4l4 4 4-4" stroke="#fff" stroke-width="2" fill="none"/></svg></div>
  </div>
</section>

<section class="testimonials">
  <h2 class="heading" style="top:78px;font-size:34px">PATIENT TESTIMONIALS</h2>
  <div class="divider" style="left:488px;top:142px"><i style="width:95px"></i><b></b><i style="width:95px"></i></div>
  <div class="abs" role="img" aria-label="Patient portrait" style="left:209px;top:203px;width:138px;height:138px;border-radius:50%;border:4px solid var(--navy);background:linear-gradient(180deg,#e9e4e0,#c9a48e)"></div>
  <svg class="abs" style="left:372px;top:212px" width="20" height="16" viewBox="0 0 20 16"><path d="M0 16V9L4 0h4L5 8h4v8zm11 0V9l4-9h4l-3 8h4v8z" fill="var(--teal)"/></svg>
  <p class="quote">&nbsp;&nbsp;&nbsp;&nbsp;&nbsp;Lorem ipsum dolor sit amet, consectetur adipiscing elit, sed do eiusmod tempor incididunt ut labore et dolore magna aliqua. Ut enim  veniam, quis nostrud exercitation ullamco laboris nisi ut aliquip ex commodo consequat. Duis aute irure dolor in reprehenderit in voluptate velit esse cillum dolore eu fugiat nulla pariatur. Excepteur sint occaecat cupidatat non proident, sunt in culpa qui officia</p>
  <div class="abs" style="left:600px;top:325px;width:400px;height:1px;background:var(--line)"></div>
  <div class="abs" style="left:815px;top:342px;font-size:13px;color:#444">– Jenny Marlowe</div>
  <div class="abs" style="left:735px;top:362px;font-size:14px;color:#c4c8cc;letter-spacing:3px">★★★★★</div>
  <div class="dots"><span></span><span></span><span></span></div>
</section>

<section class="cta">
  <h3>LOREM IPSUM DOLOR SIT AMET, CONSECTETUR ADIPISCING ELIT,<br>SED DO EIUSMOD TEMPOR INCIDIDUNT UT LABORE ET</h3>
  <div class="btn-wrap" style="left:492px;top:186px">
    <div class="btn" style="width:170px">Contact Us Today</div>
    <div class="btn-arrow"><svg width="12" height="12" viewBox="0 0 12 12"><path d="M2 4l4 4 4-4" stroke="#fff" stroke-width="2" fill="none"/></svg></div>
  </div>
</section>

<section class="contact">
  <h2 class="heading" style="top:80px;font-size:34px">LET'S GET IN TOUCH</h2>
  <div class="divider" style="left:488px;top:142px"><i style="width:95px"></i><b></b><i style="width:95px"></i></div>
  <p class="abs" style="left:0;width:1200px;top:178px;text-align:center;font-size:15px;color:#333">Get Started 123-456-7890 or Schedule A Consultation</p>
  <div class="field" style="left:324px;top:217px;width:270px">NAME</div>
  <div class="field" style="left:613px;top:217px;width:263px">EMAIL</div>
  <div class="field" style="left:324px;top:269px;width:270px">PHONE</div>
  <div class="field" style="left:613px;top:269px;width:263px">SERVICES
    <svg class="abs" style="right:12px;top:15px" width="12" height="8" viewBox="0 0 12 8"><path d="M1 1l5 5 5-5" stroke="#777" stroke-width="1.6" fill="none"/></svg>
  </div>
  <div class="field" style="left:324px;top:321px;width:552px;height:89px">MESSAGE</div>
  <div class="submit">SCHEDULE NOW!</div>
</section>

<nav class="foot-nav">
  <ul><li>HOME</li><li>ABOUT US</li><li>SERVICES</li><li>SCIENCE</li><li>TESTIMONIALS</li><li>CONTACT US</li></ul>
</nav>

<footer class="site-footer">
  <div class="abs brand" style="left:110px;top:80px;font-size:32px;gap:10px"><span class="brand-dot" style="width:20px;height:20px"></span>VARDEN</div>

  <h4 style="left:370px;top:36px">Sign Up For Newsletter</h4>
  <div class="abs" style="left:370px;top:80px;width:243px;height:38px;border:1px solid var(--line);font-size:12px;color:#555;padding:10px 10px">Enter Your Email Here</div>
  <div class="abs" style="left:622px;top:80px;width:72px;height:38px;background:var(--teal);display:flex;align-items:center;justify-content:center">
    <svg width="24" height="16" viewBox="0 0 24 16"><rect x="1" y="1" width="22" height="14" fill="none" stroke="#fff" stroke-width="2"/><path d="M1 1l11 8 11-8" fill="none" stroke="#fff" stroke-width="2"/></svg>
  </div>
  <h4 style="left:370px;top:150px">Connect With Us</h4>
  <div class="social">
    <span style="background:#3b5d9a"></span><span style="background:#2aa3db"></span><span style="background:#d2453a"></span><span style="background:#e79a2e"></span>
  </div>

  <h4 style="left:781px;top:36px">Contact Details</h4>
  <div class="contact-line" style="top:74px">
    <svg width="12" height="16" viewBox="0 0 12 16"><path d="M6 0a6 6 0 0 1 6 6c0 4-6 10-6 10S0 10 0 6a6 6 0 0 1 6-6z" fill="var(--teal)"/><circle cx="6" cy="6" r="2" fill="#fff"/></svg>
    <span style="font-size:12px;line-height:17px">VARDEN ( INSTITUTE FOR RESTORATIVE CARE )<br>Lorem ipsum dolor sit amet, consectetur adipiscing</span>
  </div>
  <div class="contact-line" style="top:116px">
    <svg width="14" height="14" viewBox="0 0 24 24"><path fill="var(--teal)" d="M6.6 10.8a15 15 0 0 0 6.6 6.6l2.2-2.2c.3-.3.7-.4 1-.2 1.1.4 2.3.6 3.6.6.6 0 1 .4 1 1V20c0 .6-.4 1-1 1A17 17 0 0 1 3 4c0-.6.4-1 1-1h3.5c.6 0 1 .4 1 1 0 1.3.2 2.5.6 3.6.1.3 0 .7-.2 1z"/></svg>
    <span>(123) 456 7890</span>
  </div>
  <div class="contact-line" style="top:152px">
    <svg width="14" height="12" viewBox="0 0 24 16"><rect x="1" y="1" width="22" height="14" fill="var(--teal)"/><path d="M1 1l11 8 11-8" fill="none" stroke="#fff" stroke-width="2"/></svg>
    <span>info@varden.example</span>
  </div>
</footer>

<div class="abs copyright" style="left:0;width:1200px">Copyright © 2018 Varden Institute For Restorative Care . All Rights Reserved.</div>

</body>
</html>
```